Prairie Wellhead Gear Depot Web Template
Oilfield Equipment web site development
Also #76 shows off shore ...........
thanks,
CraftyPixelSmith
ZorbIx
Hi PH,
please feel free to let me know the required changes so that your expectations are met.
Awaiting for your kind feedback
Designers: Thank you for all of your submitted drafts. The few that remain on the page are what I am look for in terms of a home page. Please keep the designs coming, I really appreciate all of your hard work. Everything looks great so far. I would like to keep the images land related. Ex: no offshore rig pictures. Our targeted area is for onshore production not offshore.
DRAFT # 9 IS AN EXAMPLE OF THE TYPE OF HOME PAGE TEMPLATE I AM LOOKING FOR.
NOTE: PRAIRIE WELLHEAD GEAR DEPOT IS SINGULAR. THE WORD EQUIPMENT SHOULD NEVER HAVE AN "S" AT THE END OF THE WORD. EX: DRAFTS # 4-9 SHOULD NOT HAVE A "S" AT THE END OF EQUIPMENT IN "WELCOME TO PRAIRIE WELLHEAD GEAR(S) DEPOT". ALSO IN "FEATURED EQUIPMENT(S).
Just a thought.....I would like to have the ability to show the current crude oil prices shown in a graph that is updated daily. Ex: www.barrel-rates-demo.net
I would like the logo to be larger than in Drafts #1-3.
Icon "equipment for sale" is singular and not plural
The website will be strictly to advertise equipment for sale and customers will not be able to purchase equipment through a shopping cart.
In drafts # 1-3, lets change "featured articles" to "featured equipment".
Website template should have 5 icons.
1st icon: home
2nd icon: about us
3rd icon: services
4th icon: equipment for sale
5th icon: contact us
Quick reminder:
I would like to keep “offshore rig pictures” off the home page. The equipment that is being sold is for the oil and gas industry but mainly used onshore in the production side of things.
I like the clean lines on draft #1. Draft # 1 is definitely on the right track. Keep up the good work. I look forward to seeing everyone’s drafts.

```html
<!DOCTYPE html>
<html lang="en">
<head>
<meta charset="utf-8">
<title>Prairie Wellhead Gear Depot</title>
<link rel="stylesheet" href="https://fonts.googleapis.com/css2?family=Archivo+Black&family=PT+Sans:wght@400;700&family=PT+Sans+Narrow:wght@700&display=swap">
<style>
:root{
  --red:#d9141b;
  --red-dark:#a80d12;
  --black:#151515;
  --charcoal:#2a2a2a;
  --grey-bg:#e9e9e9;
  --grey-line:#cfcfcf;
  --text:#555;
  --text-light:#8a8a8a;
  --white:#fff;
}
*{box-sizing:border-box;margin:0;padding:0}
html,body{width:1200px;height:1035px;overflow:hidden}
body{
  position:relative;
  font-family:"PT Sans",Arial,sans-serif;
  color:var(--text);
  background:linear-gradient(#dcdcdc 0,#f2f2f2 120px,#ffffff 420px,#ffffff 780px,#e7e7e7 1035px);
}
.page{position:absolute;left:240px;top:0;width:726px;height:1035px}

/* header */
.logo{position:absolute;left:6px;top:22px;display:flex;align-items:center;gap:10px}
.logo-dot{width:46px;height:46px;border-radius:50%;background:var(--red)}
.logo-name{font-family:"Archivo Black",Arial,sans-serif;font-size:34px;line-height:34px;color:var(--black);letter-spacing:1px}
.logo-tag{font-family:"PT Sans Narrow",Arial,sans-serif;font-size:10px;color:var(--red);letter-spacing:.6px;margin-top:2px}
.account-links{position:absolute;right:6px;top:8px;font-size:10px;color:#666}
.phone-box{
  position:absolute;right:0;top:28px;width:230px;height:48px;border-radius:24px;
  background:linear-gradient(#fdfdfd,#d9d9d9);border:1px solid #c4c4c4;
  display:flex;align-items:center;padding-left:8px;gap:12px;
}
.phone-icon{width:34px;height:34px;border-radius:50%;background:var(--charcoal);display:flex;align-items:center;justify-content:center}
.phone-lines{font-size:12px;color:#333;line-height:16px;text-align:right}
.phone-lines b{color:var(--black)}

/* navigation */
.main-nav{
  position:absolute;left:0;top:84px;width:726px;height:28px;
  background:linear-gradient(#2e2e2e,#0c0c0c);display:flex;align-items:center;
}
.main-nav a{
  color:var(--white);font-family:"PT Sans Narrow",Arial,sans-serif;font-size:14px;
  text-decoration:none;padding:0 11px;height:28px;line-height:28px;border-right:1px solid #444;
}
.main-nav a.active{background:var(--charcoal);border-bottom:3px solid var(--red)}
.main-nav .search{
  margin-left:auto;margin-right:6px;width:140px;height:18px;background:var(--white);
  display:flex;align-items:center;justify-content:space-between;padding:0 4px;
  font-size:10px;color:#999;
}

/* hero */
.hero{
  position:absolute;left:0;top:126px;width:726px;height:270px;background:var(--black);
  box-shadow:0 4px 10px rgba(0,0,0,.35);
}
.hero-copy{position:absolute;left:20px;top:22px;width:220px;color:#cfcfcf}
.hero-copy h1{font-family:"PT Sans Narrow",Arial,sans-serif;font-size:25px;line-height:25px;color:var(--white);letter-spacing:.5px}
.hero-copy h2{font-family:"PT Sans Narrow",Arial,sans-serif;font-size:19px;color:var(--red);margin-bottom:8px}
.hero-copy p{font-size:10.5px;line-height:14px}
.btn-read{
  position:absolute;left:20px;top:178px;width:138px;height:30px;background:var(--red);
  color:var(--white);font-size:12px;line-height:30px;text-align:center;font-weight:700;
}
.hero-photo{
  position:absolute;left:262px;top:0;width:464px;height:270px;
  background:linear-gradient(160deg,#5f7d8c 0%,#3d5f70 35%,#8a8f84 55%,#9a6a3e 70%,#3c5562 100%);
}

/* tabs */
.feature-tabs{position:absolute;left:18px;top:398px;width:690px;height:56px;display:flex;
  background:linear-gradient(#f7f7f7,#d6d6d6);box-shadow:0 4px 8px rgba(0,0,0,.2)}
.feature-tabs span{flex:1;text-align:center;line-height:56px;font-family:"PT Sans Narrow",Arial,sans-serif;
  font-size:19px;color:var(--black);border-right:1px solid var(--grey-line)}
.feature-tabs span.active{background:var(--red);color:var(--black);position:relative;top:-6px;height:62px;line-height:68px}

/* clients */
.clients{position:absolute;left:4px;top:482px;width:718px;height:66px;background:var(--white);
  border:1px solid var(--grey-line);box-shadow:0 3px 8px rgba(0,0,0,.2);display:flex;align-items:center}
.clients-title{font-family:"PT Sans Narrow",Arial,sans-serif;font-size:22px;color:var(--black);padding:0 14px}
.client-name{font-weight:700;font-size:15px;margin-right:16px}
.quote-btn{margin-left:auto;height:66px;width:150px;background:var(--red);display:flex;align-items:center;gap:8px;padding-left:8px;
  font-family:"PT Sans Narrow",Arial,sans-serif;font-size:19px;color:var(--white)}
.quote-arrow{width:30px;height:30px;background:var(--black);display:flex;align-items:center;justify-content:center}

/* info columns */
.info-col{position:absolute;top:588px;width:200px}
.info-col h3{display:flex;align-items:center;gap:10px;font-family:"PT Sans Narrow",Arial,sans-serif;font-size:20px;color:var(--black);margin-bottom:12px}
.info-col p{font-size:10px;line-height:14px;color:var(--text-light);margin-bottom:10px}
.info-col .more{font-size:10px;color:var(--charcoal);text-decoration:underline}
.col-icon{width:26px;height:26px;border-radius:50%;background:#555}
.testimonial{margin-bottom:8px}
.testimonial b{display:block;font-size:10px;color:var(--red);font-weight:400}
.testimonial span{font-size:10px;color:var(--text-light);line-height:13px}

/* footer */
.swoosh{position:absolute;left:-240px;top:800px;width:1200px;height:140px;overflow:hidden}
.footer{position:absolute;left:0;top:838px;width:726px;height:184px;background:linear-gradient(#1a1a1a,#0a0a0a);
  box-shadow:0 4px 10px rgba(0,0,0,.3)}
.footer-corner{position:absolute;right:0;top:0;width:0;height:0;border-top:16px solid var(--red);border-left:16px solid transparent}
.newsletter{position:absolute;left:18px;top:18px;display:flex;gap:12px;align-items:center}
.newsletter span{width:222px;height:22px;background:#2b2b2b;border:1px solid #3a3a3a;font-size:10px;color:#888;line-height:20px;padding-left:10px}
.newsletter b{width:110px;height:26px;background:var(--red);color:var(--white);font-family:"PT Sans Narrow",Arial,sans-serif;font-size:16px;text-align:center;line-height:26px}
.footer-links{position:absolute;left:18px;top:74px;font-size:10px;color:#aaa}
.copyright{position:absolute;left:18px;top:90px;font-size:10px;color:#888}
.socials{position:absolute;left:18px;top:144px;display:flex;gap:8px}
.socials i{width:16px;height:16px;border-radius:3px;background:#3c6fb0}
.socials i:nth-child(3){background:var(--red)}
.locations{position:absolute;left:500px;top:60px;font-size:11px;color:#ddd}
.map{position:absolute;left:500px;top:80px;width:200px;height:90px;background:radial-gradient(ellipse at center,#4a4a4a,#262626 70%)}
</style>
</head>
<body>
<div class="page">

  <header>
    <div class="logo">
      <div class="logo-dot"></div>
      <div>
        <div class="logo-name">PRAIRIE</div>
        <div class="logo-tag">WELLHEAD GEAR DEPOT</div>
      </div>
    </div>
    <div class="account-links">Login | Register | Help</div>
    <div class="phone-box">
      <div class="phone-icon">
        <svg width="18" height="18" viewBox="0 0 24 24"><path fill="#fff" d="M6.6 10.8a15 15 0 0 0 6.6 6.6l2.2-2.2c.3-.3.7-.4 1-.2 1.1.4 2.3.6 3.6.6.6 0 1 .4 1 1V20c0 .6-.4 1-1 1C10.6 21 3 13.4 3 4c0-.6.4-1 1-1h3.5c.6 0 1 .4 1 1 0 1.3.2 2.5.6 3.6.1.3 0 .7-.2 1z"/></svg>
      </div>
      <div class="phone-lines"><b>Free phone :</b> (555) 014-2270<br><b>Phone :</b> (555) 019-3384</div>
    </div>
  </header>

  <nav class="main-nav">
    <a class="active">Home</a><a>About Us</a><a>Services</a><a>Equipment for sale</a><a>Contact Us</a>
    <div class="search">Search
      <svg width="12" height="12" viewBox="0 0 24 24"><circle cx="10" cy="10" r="7" fill="none" stroke="#333" stroke-width="3"/><line x1="15" y1="15" x2="22" y2="22" stroke="#333" stroke-width="3"/></svg>
    </div>
  </nav>

  <section class="hero">
    <div class="hero-copy">
      <h1>WELCOME TO PRAIRIE</h1>
      <h2>Wellhead Gear Depot</h2>
      <p>Quality used and reconditioned wellhead gear for onshore production. Browse pumps, tanks, separators and valves checked by our crew and ready to ship to your lease this week.</p>
    </div>
    <div class="btn-read">Read More &gt;</div>
    <div class="hero-photo" role="img" aria-label="Photo of an oil production platform"></div>
  </section>

  <div class="feature-tabs">
    <span>Deep Water</span><span class="active">Our Company</span><span>Our Challanges</span><span>Clean Energy</span>
  </div>

  <section class="clients">
    <div class="clients-title">Our Clients</div>
    <span class="client-name" style="color:#1b4a9c">Ridgeline</span>
    <span class="client-name" style="color:#333">Plainsmark</span>
    <span class="client-name" style="color:#d9141b">Ostrava</span>
    <span class="client-name" style="color:#1b4a9c">Vantor</span>
    <span class="client-name" style="color:#c99a00">Cobble</span>
    <span class="client-name" style="color:#2f8a2f">Halden</span>
    <div class="quote-btn">
      <div class="quote-arrow"><svg width="14" height="14" viewBox="0 0 14 14"><path d="M4 1l6 6-6 6" fill="none" stroke="#fff" stroke-width="2.5"/></svg></div>
      Get A Quote
    </div>
  </section>

  <section class="info-col" style="left:0">
    <h3><span class="col-icon"></span>Who we are</h3>
    <p>We are a family run supplier serving onshore operators across the plains for over twenty years.</p>
    <p>Every unit is inspected, tested and priced fairly so your wells keep producing without delay.</p>
    <span class="more">read more &gt;</span>
  </section>

  <section class="info-col" style="left:264px">
    <h3><span class="col-icon" style="background:#888"></span>Solutions</h3>
    <p>From pump jacks to heater treaters, we source the gear you need and deliver it to your site. Ask about trade-in, hauling and setup by our field team for a smooth start.</p>
    <span class="more">read more &gt;</span>
  </section>

  <section class="info-col" style="left:526px">
    <h3><svg width="28" height="28" viewBox="0 0 24 24"><path fill="#d9141b" d="M12 1l3.4 7 7.6 1-5.5 5.3 1.3 7.6L12 18.3l-6.8 3.6 1.3-7.6L1 9l7.6-1z"/></svg>Testimonial</h3>
    <div class="testimonial"><b>Mark R.</b><span>Fast delivery and the pump ran perfectly from day one.</span></div>
    <div class="testimonial"><b>Lena T.</b><span>Honest pricing and a crew that knows oilfield work.</span></div>
    <div class="testimonial"><b>Dale W.</b><span>Our tank battery was set up on time and on budget.</span></div>
  </section>

  <svg class="swoosh" viewBox="0 0 1200 140" preserveAspectRatio="none">
    <path d="M0 140 Q600 -40 1200 140 Z" fill="#d6d6d6"/>
  </svg>

  <footer class="footer">
    <div class="footer-corner"></div>
    <div class="newsletter"><span>Your Name</span><span>Email address</span><b>subscribe</b></div>
    <div class="footer-links">Home | About Us | Services | Products | Testimonials | Contact Us</div>
    <div class="copyright">Copyright © 2011 Prairie . All Rights Reserved.</div>
    <div class="socials"><i></i><i></i><i></i><i></i></div>
    <div class="locations">Our Locations</div>
    <div class="map" role="img" aria-label="World map of company locations"></div>
  </footer>

</div>
</body>
</html>
```